New website design

Hello again, we need you to create a basic, standard website with a homepage, 'contact us' page with reply form, 'pricing page' and 'about us' page. We would like to see most design elements carried over from www.pilvarotek.com, our primary website. You can also use the front page of the attached brochure as inspiration for the homepage. The second attachment shows the pricing page (image on the right) with vertical columns - that's a good template for you to use on the pricing page for the website. The third attachment contains the text for the pricing page...just don't use that layout, try and duplicate the vertical layout example.
Target Market(s)
hospitals/medical care facilities
Coding
Coded - Design and coding required
Number of Pages Required
4 page

```html
<!DOCTYPE html>
<html lang="en">
<head>
<meta charset="utf-8">
<title>Kestrel Medical — Quality Assembly and Packaging</title>
<link rel="stylesheet" href="https://fonts.googleapis.com/css2?family=Exo+2:wght@500;600;700&family=Poppins:wght@300;400;500;600;700&display=swap">
<style>
:root{
  --blue:#0f65a3;
  --blue-deep:#0b4f82;
  --blue-dark:#0a3d66;
  --ink:#111418;
  --text:#6f7680;
  --pale:#eef4f8;
  --white:#ffffff;
  --footer:#121416;
}
*{box-sizing:border-box;margin:0;padding:0}
html,body{width:1200px;height:4501px;overflow:hidden;background:var(--white)}
body{font-family:"Poppins",sans-serif;color:var(--ink)}
.page{position:relative;width:1200px;height:4501px;overflow:hidden}
.abs{position:absolute}
.shapes{position:absolute;left:0;top:0}
.heading{font-family:"Exo 2",sans-serif;font-weight:700;letter-spacing:.5px}
.heading .accent{color:var(--blue)}
.ghost{position:absolute;font-family:"Exo 2",sans-serif;font-weight:700;color:transparent;-webkit-text-stroke:1px rgba(15,101,163,.12);white-space:nowrap}
.btn{position:absolute;background:var(--blue);color:var(--white);font-weight:600;font-size:13px;letter-spacing:.5px;display:flex;align-items:center;justify-content:center;border-radius:3px;text-transform:uppercase}

/* header */
.brand{position:absolute;left:60px;top:18px;display:flex;align-items:center;gap:12px;color:var(--white);font-size:40px;font-weight:500}
.brand .dot{width:36px;height:36px;border-radius:50%;background:var(--blue)}
.nav{position:absolute;top:28px;left:590px;display:flex;gap:30px;font-size:12px;color:var(--white);text-transform:uppercase}
.call{position:absolute;left:998px;top:16px;width:142px;height:38px;background:var(--blue);color:var(--white);font-weight:600;font-size:14px;display:flex;align-items:center;justify-content:center;border-radius:4px}

.hero-title{position:absolute;left:61px;top:218px;color:var(--white);font-size:50px;line-height:60px;font-family:"Exo 2",sans-serif;font-weight:600}
.hero-text{position:absolute;left:61px;top:364px;width:420px;color:var(--white);font-size:12px;line-height:20px}

/* feature cards */
.feature{position:absolute;top:559px;width:236px}
.feature .photo{height:188px;border:3px solid var(--white);box-shadow:0 6px 18px rgba(0,0,0,.15)}
.feature .label{position:relative;margin:0 auto;width:180px;height:62px;margin-top:-18px;background:var(--white);box-shadow:0 6px 16px rgba(0,0,0,.12);display:flex;align-items:center;justify-content:center;text-align:center;font-size:13px;font-weight:500;line-height:20px;padding-top:12px}
.arrow-dot{position:absolute;width:30px;height:30px;border-radius:50%;background:var(--blue);border:2px solid var(--white);display:flex;align-items:center;justify-content:center}
.feature .arrow-dot{left:50%;top:-16px;transform:translateX(-50%)}

/* about */
.about-photo{position:absolute;left:143px;top:870px;width:374px;height:322px;border-radius:10px;background:linear-gradient(135deg,#cfe3f2,#7fa9cc 55%,#4b7aa3)}
.about-title{position:absolute;left:646px;top:872px;font-size:32px}
.para{font-size:12px;line-height:19px;color:var(--text)}
.ticks{position:absolute;left:646px;top:1066px;width:290px;list-style:none}
.ticks li{position:relative;padding-left:26px;font-size:12px;line-height:19px;color:#333;margin-bottom:14px}
.ticks li::before{content:"";position:absolute;left:0;top:3px;width:14px;height:14px;border-radius:50%;background:var(--blue)}

/* navigate */
.nav-headline{position:absolute;left:61px;top:1462px;width:590px;font-size:31px;line-height:38px;font-weight:700}
.circle{position:absolute;border-radius:50%;background:var(--white);box-shadow:0 8px 24px rgba(15,60,100,.1);display:flex;flex-direction:column;align-items:center;justify-content:center;text-align:center;font-size:15px;font-weight:500;line-height:22px}
.circle svg{margin-bottom:6px}

/* pricing */
.section-title{position:absolute;font-size:31px;text-transform:uppercase}
.price-card{position:absolute;top:2036px;width:286px;height:360px;background:var(--white);padding:26px 28px 0}
.price-card .tag{font-size:10px;line-height:14px;font-weight:600}
.price-card .name{font-size:20px;line-height:26px;font-weight:600;margin-top:8px}
.price-card .rate{color:var(--blue);font-size:21px;line-height:28px;font-weight:600;margin-top:2px}
.price-card .rate small{font-size:11px;color:var(--text);font-weight:400;margin-left:8px}
.price-card .lead{font-size:11.5px;line-height:19px;margin-top:10px}
.price-card .para{font-size:11px;line-height:19.5px;margin-top:10px;max-height:98px;overflow:hidden}
.price-card .btn{left:28px;top:302px;width:114px;height:36px;font-size:11px}

/* services */
.service{position:absolute;top:2698px;width:188px;text-align:center}
.service .pill{height:272px;border-radius:94px 94px 94px 94px/140px 140px 140px 140px}
.service .arrow-dot{left:50%;top:257px;transform:translateX(-50%)}
.service .caption{margin-top:34px;font-size:15px;font-weight:500;line-height:23px}

/* sterilization */
.steril-text{position:absolute;left:340px;top:3320px;width:520px;text-align:center;color:var(--white);font-size:12px;line-height:20px}
.play{position:absolute;left:525px;top:3460px;width:56px;height:56px;border-radius:50%;border:3px solid rgba(255,255,255,.6);background:var(--white);display:flex;align-items:center;justify-content:center}
.play-label{position:absolute;left:594px;top:3478px;color:var(--white);font-size:12px;font-weight:600}

/* team */
.team-title{position:absolute;left:114px;top:3748px;font-size:31px}
.member-name{position:absolute;left:114px;top:3818px;font-size:12px;font-weight:600}
.member-role{position:absolute;left:114px;top:3836px;font-size:11px;color:var(--text)}
.member-bio{position:absolute;left:114px;top:3874px;width:390px}
.thumb{position:absolute;top:4002px;width:52px;height:52px;border-radius:50%;background:linear-gradient(160deg,#bcc7d2,#5d6b7a)}
.thumb.active{border:3px solid var(--white);box-shadow:0 0 0 2px var(--blue)}
.portrait{position:absolute;left:757px;top:3750px;width:300px;height:300px;border-radius:50%;background:radial-gradient(circle at 50% 40%,#e8edf1,#b9c3cc 60%,#8c99a6)}

/* footer */
.foot-brand{position:absolute;left:0;width:1200px;top:4208px;display:flex;justify-content:center;align-items:center;gap:10px;color:var(--white);font-size:32px;font-weight:500}
.foot-brand .dot{width:30px;height:30px;border-radius:50%;background:var(--blue)}
.foot-links{position:absolute;left:0;width:1200px;top:4288px;display:flex;justify-content:center;gap:18px;color:#cfd4d9;font-size:12px}
.foot-links span.sep{color:#777}
.contact{position:absolute;top:4348px;display:flex;gap:12px;color:#cfd4d9;font-size:12px;line-height:18px}
.contact .ico{width:34px;height:34px;border-radius:50%;background:var(--white);flex:none;display:flex;align-items:center;justify-content:center}
.copyright{position:absolute;left:0;width:1200px;top:4468px;text-align:center;color:#cfd4d9;font-size:11px}
</style>
</head>
<body>
<div class="page">

<svg class="shapes" width="1200" height="4501" viewBox="0 0 1200 4501" aria-hidden="true">
  <defs>
    <linearGradient id="heroFill" x1="0" y1="0" x2="1" y2="1">
      <stop offset="0" stop-color="#5b6a78"/>
      <stop offset=".55" stop-color="#9aa7b3"/>
      <stop offset="1" stop-color="#c9d2da"/>
    </linearGradient>
    <linearGradient id="blueFill" x1="0" y1="0" x2="1" y2="1">
      <stop offset="0" stop-color="#0d5f9b"/>
      <stop offset="1" stop-color="#14689f"/>
    </linearGradient>
    <linearGradient id="sterFill" x1="0" y1="0" x2="1" y2="1">
      <stop offset="0" stop-color="#1a6aa4"/>
      <stop offset=".5" stop-color="#2a7ab4"/>
      <stop offset="1" stop-color="#0d5c96"/>
    </linearGradient>
  </defs>
  <path role="img" aria-label="Gloved hand loading a sterilization chamber" d="M0 0H1200V150L1050 520Q1020 600 950 628Q900 638 840 638H0Z" fill="url(#heroFill)"/>
  <path d="M0 0H1200V150L1050 520Q1020 600 950 628Q900 638 840 638H0Z" fill="rgba(10,40,70,.25)"/>
  <polygon points="1200,160 1200,230 1045,572 1022,572" fill="var(--blue)"/>

  <path d="M0 1360Q0 1305 70 1298L1080 1284Q1200 1282 1200 1370V1895H0Z" fill="var(--pale)"/>

  <path role="img" aria-label="Blue laboratory texture behind pricing" d="M0 1950Q0 1830 120 1828L1060 1890Q1200 1900 1200 2010V2410Q1200 2468 1120 2475L120 2540Q0 2548 0 2440Z" fill="url(#blueFill)"/>

  <path role="img" aria-label="Gloved hands handling sterile packaging" d="M0 3230Q0 3185 80 3178L1100 3108Q1200 3102 1200 3200V3580Q1200 3640 1110 3648L0 3668Z" fill="url(#sterFill)"/>

  <circle cx="808" cy="3780" r="38" fill="var(--blue)"/>
  <circle cx="852" cy="3765" r="30" fill="none" stroke="#d7dde3" stroke-width="1.5"/>
  <circle cx="955" cy="4055" r="38" fill="var(--blue)"/>
  <circle cx="1000" cy="4005" r="20" fill="none" stroke="#d7dde3" stroke-width="1.5"/>

  <rect x="0" y="4140" width="1200" height="361" fill="var(--footer)"/>
  <polygon points="130,4190 155,4190 40,4501 10,4501" fill="var(--blue)"/>
</svg>

<!-- header -->
<div class="brand"><span class="dot"></span>Kestrel Medical</div>
<nav class="nav"><span>Home</span><span>Services</span><span>About Us</span><span>Pricing</span><span>Support</span></nav>
<div class="call">(555) 014-2290</div>

<h1 class="hero-title">Quality Assembly and<br>Packaging</h1>
<p class="hero-text">Kestrel Medical is certified to requirements of ISO 13485:2016 for contract packaging and sterilization of medical products.</p>
<div class="btn" style="left:61px;top:442px;width:126px;height:38px">Contact Us</div>

<!-- features -->
<div class="feature" style="left:75px">
  <div class="photo" role="img" aria-label="Technicians assembling devices in a cleanroom" style="background:linear-gradient(135deg,#c8dcec,#6f9cc6)"></div>
  <div class="label"><span class="arrow-dot"><svg width="14" height="10" viewBox="0 0 14 10"><path d="M1 5H12M8 1L12 5L8 9" stroke="#fff" stroke-width="1.8" fill="none"/></svg></span>Contract Assembly &amp;<br>Packaging</div>
</div>
<div class="feature" style="left:337px">
  <div class="photo" role="img" aria-label="Packaging machinery line" style="background:linear-gradient(135deg,#dfe4e8,#8d99a4)"></div>
  <div class="label"><span class="arrow-dot"><svg width="14" height="10" viewBox="0 0 14 10"><path d="M1 5H12M8 1L12 5L8 9" stroke="#fff" stroke-width="1.8" fill="none"/></svg></span>Support Services</div>
</div>
<div class="feature" style="left:608px">
  <div class="photo" role="img" aria-label="Sterilizer chamber filled with trays" style="background:linear-gradient(135deg,#b9c4cd,#4d6f8f)"></div>
  <div class="label"><span class="arrow-dot"><svg width="14" height="10" viewBox="0 0 14 10"><path d="M1 5H12M8 1L12 5L8 9" stroke="#fff" stroke-width="1.8" fill="none"/></svg></span>Inventory Control</div>
</div>

<!-- about -->
<div class="about-photo" role="img" aria-label="Cleanroom with technicians at workbenches"></div>
<div class="ghost" style="left:780px;top:858px;font-size:56px">ABOUT US</div>
<h2 class="heading about-title">ABOUT <span class="accent">US</span></h2>
<p class="para abs" style="left:646px;top:928px;width:410px">Kestrel offers deep and vast knowledge in the realm of sterilization and, in particular, detailed guidance with our vertically integrated Hydrogen Peroxide Gas Plasma sterilization modality.</p>
<p class="para abs" style="left:646px;top:994px;width:410px">Assistance with the development and comparisons of full validation and batch release can be provided to OEMs to help you select the best path forward for your project.</p>
<ul class="ticks">
  <li>Kestrel Medical Inc. offers efficient and FDA compliant assembly</li>
  <li>packaging and in-house Hydrogen Peroxide Gas Plasma (HPGP) specific</li>
  <li>idation services for manufacturing processes</li>
</ul>

<!-- navigate -->
<h2 class="nav-headline">Allow us to help you navigate every regulatory hurdle that comes with bringing your product to market</h2>
<p class="para abs" style="left:61px;top:1606px;width:340px;color:#444">Kestrel Medical is committed to providing our customers with continued assurance of compliance with today's evolving regulatory requirements.</p>
<div class="btn" style="left:61px;top:1703px;width:142px;height:36px">Contact Us</div>

<div class="circle" style="left:833px;top:1376px;width:210px;height:210px">
  <svg width="44" height="58" viewBox="0 0 44 58"><path d="M10 4L18 22M26 4L22 24M16 30Q10 44 20 48Q32 50 30 36L24 26Z" stroke="var(--blue)" stroke-width="3" fill="none"/><circle cx="34" cy="14" r="4" fill="var(--blue)"/></svg>
  Our<br>Facility</div>
<div class="circle" style="left:688px;top:1495px;width:126px;height:126px">
  <svg width="36" height="36" viewBox="0 0 36 36"><circle cx="18" cy="18" r="15" stroke="var(--blue)" stroke-width="3" fill="none"/><path d="M3 18H33M18 3Q8 18 18 33M18 3Q28 18 18 33" stroke="var(--blue)" stroke-width="2.5" fill="none"/></svg>
  Our<br>Location</div>
<div class="circle" style="left:735px;top:1638px;width:164px;height:164px">
  <svg width="52" height="52" viewBox="0 0 52 52"><circle cx="26" cy="26" r="18" fill="none" stroke="var(--blue)" stroke-width="6" stroke-dasharray="6 4"/><circle cx="26" cy="26" r="11" fill="var(--blue)"/><path d="M26 19L28 24H33L29 27L31 32L26 29L21 32L23 27L19 24H24Z" fill="#fff"/></svg>
  Our<br>Expertise</div>
<div class="circle" style="left:920px;top:1596px;width:154px;height:154px">
  <span style="color:var(--blue);font-size:30px;font-family:'Exo 2',sans-serif;font-weight:600;line-height:38px">20,000</span>square<br>foot</div>

<!-- pricing -->
<div class="ghost" style="left:392px;top:1950px;font-size:52px;-webkit-text-stroke:1px rgba(255,255,255,.15)">PRICING LIST</div>
<h2 class="heading section-title" style="left:0;width:1200px;text-align:center;top:1958px;color:var(--white)">Our Pricing</h2>

<div class="price-card" style="left:155px">
  <div class="tag">UNSCHEDUAL</div><div class="name">ON SITE</div>
  <div class="rate">$225<small>/HOUR *</small></div>
  <p class="lead">Emergency Priority service Technicians Typically On-Premeses Within 24 Hours</p>
  <p class="para">Electronic device Failure is one of the few certainties in life. we don't know when mission critical devices will malfiction,but if were prepared and have</p>
  <div class="btn">Book Now</div>
</div>
<div class="price-card" style="left:471px">
  <div class="tag">UNSCHEDUAL</div><div class="name">ON SITE</div>
  <div class="rate">$225<small>/HOUR *</small></div>
  <p class="lead">Emergency Priority service Technicians Typically On-Premeses Within 24 Hours</p>
  <p class="para">Electronic device Failure is one of the few certainties in life. we don't know when mission critical devices will malfiction,but if were prepared and have</p>
  <div class="btn">Book Now</div>
</div>
<div class="price-card" style="left:786px">
  <div class="tag">UNSCHEDUAL</div><div class="name">ON SITE</div>
  <div class="rate">$225<small>/HOUR *</small></div>
  <p class="lead">Emergency Priority service Technicians Typically On-Premeses Within 24 Hours</p>
  <p class="para">Electronic device Failure is one of the few certainties in life. we don't know when mission critical devices will malfiction,but if were prepared and have</p>
  <div class="btn">Book Now</div>
</div>

<!-- services -->
<div class="ghost" style="left:150px;top:2620px;font-size:52px">SERVICES</div>
<h2 class="heading section-title" style="left:72px;top:2634px">Our <span class="accent">Services</span></h2>

<div class="service" style="left:71px"><div class="pill" role="img" aria-label="Sterilization equipment glowing blue" style="background:linear-gradient(160deg,#8fd0f5,#1673b8)"></div><span class="arrow-dot"><svg width="14" height="10" viewBox="0 0 14 10"><path d="M1 5H12M8 1L12 5L8 9" stroke="#fff" stroke-width="1.8" fill="none"/></svg></span><div class="caption">Sterilization</div></div>
<div class="service" style="left:289px"><div class="pill" role="img" aria-label="Technician packaging products" style="background:linear-gradient(160deg,#eef1f3,#9aa6b1)"></div><span class="arrow-dot"><svg width="14" height="10" viewBox="0 0 14 10"><path d="M1 5H12M8 1L12 5L8 9" stroke="#fff" stroke-width="1.8" fill="none"/></svg></span><div class="caption">Packaging</div></div>
<div class="service" style="left:506px"><div class="pill" role="img" aria-label="Worker in cleanroom gear at a bench" style="background:linear-gradient(160deg,#f1f3f5,#8fa3b6)"></div><span class="arrow-dot"><svg width="14" height="10" viewBox="0 0 14 10"><path d="M1 5H12M8 1L12 5L8 9" stroke="#fff" stroke-width="1.8" fill="none"/></svg></span><div class="caption">Contract Manufacturing</div></div>
<div class="service" style="left:724px"><div class="pill" role="img" aria-label="Gloved hands with surgical instruments" style="background:linear-gradient(160deg,#a9c6d8,#35627f)"></div><span class="arrow-dot"><svg width="14" height="10" viewBox="0 0 14 10"><path d="M1 5H12M8 1L12 5L8 9" stroke="#fff" stroke-width="1.8" fill="none"/></svg></span><div class="caption">New Product<br>Introduction</div></div>
<div class="service" style="left:941px"><div class="pill" role="img" aria-label="Hands opening a sterile pouch" style="background:linear-gradient(160deg,#d7dde2,#4f6a83)"></div><span class="arrow-dot"><svg width="14" height="10" viewBox="0 0 14 10"><path d="M1 5H12M8 1L12 5L8 9" stroke="#fff" stroke-width="1.8" fill="none"/></svg></span><div class="caption">Validations</div></div>

<!-- sterilization -->
<div class="ghost" style="left:190px;top:3240px;font-size:52px;-webkit-text-stroke:1px rgba(255,255,255,.15)">STERILIZATION SOLUTION</div>
<h2 class="heading section-title" style="left:0;width:1200px;text-align:center;top:3250px;color:var(--white)">Sterilization Solutions</h2>
<p class="steril-text">Kestrel Medical is committed to finding the most suitable and efficient sterilization method for our customers' products.<br>Kestrel offers deep and vast knowledge in the realm of sterilization and, in particular, detailed guidance with our vertically integrated Hydrogen Peroxide Gas Plasma sterilization modality.</p>
<div class="play"><svg width="16" height="18" viewBox="0 0 16 18"><path d="M2 1L15 9L2 17Z" fill="var(--blue)"/></svg></div>
<div class="play-label">Watch Video</div>

<!-- team -->
<div class="ghost" style="left:318px;top:3732px;font-size:58px">TEAM</div>
<h2 class="heading team-title">MEET TEAM</h2>
<div class="member-name">MARLOW PENRITH</div>
<div class="member-role">PRESIDENT AND CEO</div>
<p class="para member-bio">For nearly fifteen years, Marlow Penrith has successfully served as president for Kestrel Medical, Inc. During his tenure, Kestrel Medical has experienced significant growth in industry specific packaging and specialty sterilization services for the medical device industry.</p>
<div class="thumb" role="img" aria-label="Team member portrait" style="left:112px"></div>
<div class="thumb active" role="img" aria-label="Team member portrait" style="left:178px;background:linear-gradient(160deg,#f0d9c4,#c79b79)"></div>
<div class="thumb" role="img" aria-label="Team member portrait" style="left:250px"></div>
<div class="portrait" role="img" aria-label="Portrait of the president and CEO"></div>

<!-- footer -->
<div class="foot-brand"><span class="dot"></span>Kestrel Medical</div>
<div class="foot-links"><span>Home</span><span class="sep">|</span><span>About Us</span><span class="sep">|</span><span>Services</span><span class="sep">|</span><span>Support</span><span class="sep">|</span><span>Career</span><span class="sep">|</span><span>Contact Us</span></div>

<div class="contact" style="left:188px"><span class="ico"><svg width="14" height="18" viewBox="0 0 14 18"><path d="M7 17Q1 10 1 7A6 6 0 0 1 13 7Q13 10 7 17Z" fill="var(--blue)"/><circle cx="7" cy="7" r="2.2" fill="#fff"/></svg></span><span>418 Orchard Ln, Fairhaven, CA<br>90210</span></div>
<div class="contact" style="left:452px"><span class="ico"><svg width="16" height="12" viewBox="0 0 16 12"><rect x="1" y="1" width="14" height="10" rx="1" fill="none" stroke="var(--blue)" stroke-width="1.6"/><path d="M1 1L8 7L15 1" fill="none" stroke="var(--blue)" stroke-width="1.6"/></svg></span><span style="padding-top:8px">info@pilvarotek.com</span></div>
<div class="contact" style="left:662px"><span class="ico"><svg width="16" height="16" viewBox="0 0 16 16"><path d="M3 1L6 1L7 5L5 6Q6 9 10 11L11 9L15 10L15 13Q14 15 12 15Q1 12 1 3Q1 1 3 1Z" fill="var(--blue)"/></svg></span><span style="padding-top:8px">(555) 014-2290</span></div>
<div class="contact" style="left:826px"><span class="ico"><svg width="16" height="16" viewBox="0 0 16 16"><rect x="2" y="5" width="12" height="9" rx="1" fill="var(--blue)"/><rect x="5" y="1" width="6" height="5" fill="none" stroke="var(--blue)" stroke-width="1.5"/></svg></span><span style="padding-top:8px">(555) 014-2291</span></div>

<div class="copyright">© 2021 Kestrel Medical - All Right Reserved.</div>
</div>
</body>
</html>
```